Tallgrove Vale Management

I need a professional website. My current website is tallgrovevalemanagement.com and I hate it. It was created with some AI tool very quickly because I needed a site up and running with no advanced notice. I’m open to all designs .. I trust you, the professionals will deliver the results I’m anxiously awaiting! :)

```html
<!DOCTYPE html>
<html lang="en">
<head>
<meta charset="utf-8">
<title>Tallgrove Vale Management — Ohio Section 8 Property Management</title>
<link rel="stylesheet" href="https://fonts.googleapis.com/css2?family=Playfair+Display:wght@500;600;700&family=Inter:wght@400;500;600;700&display=swap">
<style>
:root{
  --navy:#1d2d59;
  --navy-deep:#13204a;
  --red:#c62430;
  --blush:#dc9aa0;
  --ink:#1a2238;
  --muted:#7d869c;
  --line:#e4e7ef;
  --mist:#f3f4f8;
  --white:#ffffff;
}
*{box-sizing:border-box;margin:0;padding:0}
html,body{width:1200px;height:5059px;overflow:hidden}
body{font-family:"Inter",sans-serif;color:var(--ink);background:var(--white);position:relative}
.abs{position:absolute}
.eyebrow{font-size:11px;font-weight:700;letter-spacing:2px;color:var(--red);text-transform:uppercase}
.h2{font-family:"Playfair Display",serif;font-weight:600;font-size:44px;line-height:52px;color:var(--ink)}
.body{font-size:14px;line-height:23px;color:var(--muted)}
.btn{display:inline-flex;align-items:center;gap:8px;border-radius:24px;font-size:13px;font-weight:600;padding:0 28px;height:44px}
.btn-red{background:var(--red);color:#fff}
.btn-navy{background:var(--navy);color:#fff}
.btn-ghost{border:1px solid rgba(255,255,255,.45);color:#fff}

/* hero */
.hero{top:0;left:0;width:1200px;height:752px;overflow:hidden}
.hero-photo{position:absolute;inset:0;background:linear-gradient(100deg,#3a2a2e 0%,#4a3b3f 30%,#5c5f6e 55%,#3c4563 80%,#2a3356 100%)}
.hero-shade{position:absolute;inset:0;background:linear-gradient(90deg,rgba(20,28,60,.8) 0%,rgba(20,28,60,.45) 55%,rgba(20,28,60,.55) 100%)}
.nav{top:18px;left:82px;width:1036px;height:36px;display:flex;align-items:center}
.brand{display:flex;align-items:center;gap:10px;color:#fff;font-weight:700;font-size:13px}
.brand-dot{width:30px;height:30px;border-radius:50%;background:var(--red)}
.nav-links{margin-left:auto;display:flex;gap:30px;font-size:12px;color:rgba(255,255,255,.85)}
.nav-cta{margin-left:30px;background:var(--navy);color:#fff;border-radius:20px;font-size:12px;font-weight:600;padding:10px 18px}
.hero-badge{top:150px;left:82px;background:var(--red);color:#fff;font-size:10px;font-weight:700;letter-spacing:1.5px;padding:6px 12px;border-radius:14px}
.hero-title{top:200px;left:82px;font-family:"Playfair Display",serif;font-weight:700;font-size:80px;line-height:86px;color:#fff;width:760px}
.hero-title span{color:var(--blush)}
.hero-copy{top:486px;left:82px;width:500px;font-size:15px;line-height:26px;color:rgba(255,255,255,.78)}
.hero-actions{top:596px;left:82px;display:flex;gap:12px}
.stat-box{top:487px;left:845px;width:275px;height:152px;border:1px solid rgba(255,255,255,.2);background:rgba(255,255,255,.08);border-radius:14px;display:grid;grid-template-columns:1fr 1fr;padding:18px 12px;text-align:center}
.stat-num{font-family:"Playfair Display",serif;font-size:22px;color:#fff}
.stat-lbl{font-size:9px;color:rgba(255,255,255,.6);line-height:12px}

.trust{top:752px;left:0;width:1200px;height:50px;background:var(--mist);display:flex;justify-content:center;align-items:center;gap:34px;font-size:10px;font-weight:600;letter-spacing:1px;color:#6a7390}
.trust i{display:inline-block;width:4px;height:4px;border-radius:50%;background:var(--red);margin-right:8px;vertical-align:middle}

/* about */
.about-photo-a{top:941px;left:82px;width:362px;height:363px;border-radius:12px;background:linear-gradient(160deg,#1f3360 0%,#3b5a8c 45%,#c4a37d 100%)}
.about-photo-b{top:1257px;left:326px;width:238px;height:200px;border-radius:10px;border:6px solid #fff;box-shadow:0 10px 30px rgba(20,30,60,.18);background:linear-gradient(180deg,#bcd0e4 0%,#c8b59a 60%,#7a8a6a 100%)}
.about-badge{top:1318px;left:94px;width:134px;height:86px;border-radius:10px;background:var(--navy);color:#fff;padding:14px 16px}
.about-badge b{font-family:"Playfair Display",serif;font-size:26px;font-weight:600;display:block;line-height:28px}
.about-badge small{font-size:9px;line-height:12px;color:rgba(255,255,255,.75);display:block}
.about-text{top:928px;left:634px;width:486px}
.about-text .h2{color:var(--navy);margin:14px 0 24px}
.about-text .body b{color:var(--ink);font-weight:600}
.checks{list-style:none;margin:24px 0 30px;display:flex;flex-direction:column;gap:12px;font-size:12px;font-weight:500}
.checks li{display:flex;align-items:center;gap:10px}

/* services */
.services{top:1597px;left:0;width:1200px;height:907px;background:var(--mist)}
.svc-head{top:127px;left:82px}
.svc-intro{top:188px;left:620px;width:490px}
.svc-grid{top:314px;left:82px;width:1036px;display:grid;grid-template-columns:repeat(3,1fr);gap:20px}
.card{background:#fff;border-radius:12px;height:224px;padding:28px;border:1px solid var(--line)}
.card-icon{width:36px;height:36px;border-radius:8px;background:var(--mist);display:flex;align-items:center;justify-content:center}
.card-icon.on{background:var(--navy)}
.card h3{font-size:15px;font-weight:600;margin:24px 0 10px}
.card p{font-size:12px;line-height:20px;color:var(--muted)}

/* process */
.process-head{top:2630px;left:0;width:1200px;text-align:center}
.process-head .h2{margin:8px 0 6px}
.steps{top:2826px;left:82px;width:1036px;display:grid;grid-template-columns:repeat(5,1fr)}
.step{text-align:center;position:relative;padding:0 12px}
.step-num{width:34px;height:34px;border-radius:50%;background:var(--mist);color:#6a7390;font-size:11px;font-weight:600;display:flex;align-items:center;justify-content:center;margin:0 auto 20px;position:relative;z-index:1}
.step-num.on{background:var(--red);color:#fff}
.step::after{content:"";position:absolute;top:17px;left:60%;width:80%;height:1px;background:var(--line)}
.step:last-child::after{display:none}
.step h4{font-size:13px;font-weight:600;margin-bottom:10px}
.step p{font-size:11.5px;line-height:20px;color:var(--muted)}
.cta-band{top:3089px;left:82px;width:1036px;height:173px;border-radius:18px;background:linear-gradient(90deg,#182752,#22336a);display:flex;align-items:center;padding:0 56px}
.cta-band h3{font-family:"Playfair Display",serif;font-weight:600;font-size:30px;color:#fff}
.cta-band p{font-size:13px;color:rgba(255,255,255,.65);margin-top:6px}
.cta-band .btn{margin-left:auto}

/* testimonials */
.stories{top:3388px;left:0;width:1200px;height:593px;background:var(--mist)}
.stories-head{top:169px;left:82px}
.stories-head .h2{margin-top:12px}
.arrows{top:386px;left:82px;display:flex;gap:12px}
.arrow{width:30px;height:30px;border-radius:50%;border:1px solid #cfd4e0;background:#fff;display:flex;align-items:center;justify-content:center}
.dots{top:432px;left:82px;display:flex;gap:6px}
.dots i{display:block;width:8px;height:3px;background:#cfd4e0;border-radius:2px}
.dots i.on{width:28px;background:var(--navy)}
.quote-card{top:125px;left:352px;width:766px;min-height:342px;background:#fff;border-radius:16px;box-shadow:0 12px 40px rgba(20,30,60,.08);padding:40px 42px 36px}
.stars{display:flex;gap:4px;margin-bottom:20px}
.quote{font-family:"Playfair Display",serif;font-size:25px;line-height:35px;color:var(--ink)}
.author{border-top:1px solid var(--line);margin-top:24px;padding-top:22px;display:flex;align-items:center;gap:14px}
.avatar{width:32px;height:32px;border-radius:50%;background:var(--navy);color:#fff;font-size:12px;font-weight:700;display:flex;align-items:center;justify-content:center}
.author b{font-size:12px;display:block}
.author small{font-size:10px;color:var(--muted)}

/* contact */
.contact-head{top:4108px;left:82px;width:340px}
.contact-head .h2{margin:12px 0 20px}
.contact-list{top:4370px;left:82px;display:flex;flex-direction:column;gap:30px}
.c-item{display:flex;gap:20px}
.c-icon{width:36px;height:36px;border-radius:50%;background:var(--mist);display:flex;align-items:center;justify-content:center}
.c-item small{font-size:9px;font-weight:700;letter-spacing:1px;color:var(--red);display:block;margin-bottom:4px}
.c-item b{font-size:14px;font-weight:600;line-height:20px}
.form{top:4109px;left:634px;width:486px;height:497px;background:var(--mist);border-radius:18px;padding:34px 36px}
.form h3{font-family:"Playfair Display",serif;font-weight:600;font-size:17px;margin-bottom:22px}
.row{display:grid;grid-template-columns:1fr 1fr;gap:16px}
.field{margin-bottom:18px}
.field label{display:block;font-size:9px;font-weight:700;letter-spacing:1px;color:#6a7390;margin-bottom:8px}
.input{background:#fff;border:1px solid var(--line);border-radius:8px;height:36px;padding:0 14px;font-size:12px;color:#8a92a6;display:flex;align-items:center}
.input.tall{height:86px;align-items:flex-start;padding-top:12px;line-height:18px}
.submit{height:44px;border-radius:24px;background:var(--navy);color:#fff;font-size:13px;font-weight:600;display:flex;align-items:center;justify-content:center;margin-top:6px}
.form-note{text-align:center;font-size:10px;color:var(--muted);margin-top:14px}

/* footer */
.footer{top:4733px;left:0;width:1200px;height:326px;background:var(--navy-deep);color:rgba(255,255,255,.6)}
.f-brand{top:58px;left:82px;width:290px}
.f-brand .brand{margin-bottom:18px}
.f-brand p{font-size:12px;line-height:20px}
.f-col{top:62px}
.f-col h5{font-size:10px;font-weight:700;letter-spacing:1.5px;color:#fff;margin-bottom:18px}
.f-col li{list-style:none;font-size:12px;margin-bottom:12px;display:flex;align-items:center;gap:8px}
.f-col li i{width:6px;height:6px;border-radius:50%;background:var(--red);display:inline-block}
.f-bottom{top:275px;left:82px;width:1036px;border-top:1px solid rgba(255,255,255,.1);padding-top:14px;display:flex;justify-content:space-between;font-size:10px;color:rgba(255,255,255,.4)}
</style>
</head>
<body>

<header class="abs hero">
  <div class="hero-photo" role="img" aria-label="Row of Victorian townhouses under a cloudy sky"></div>
  <div class="hero-shade"></div>
  <nav class="abs nav">
    <div class="brand"><span class="brand-dot"></span>Tallgrove Vale Management</div>
    <div class="nav-links"><span>About</span><span>Services</span><span>Process</span><span>Testimonials</span><span>Contact</span></div>
    <div class="nav-cta">Free Consultation</div>
  </nav>
  <div class="abs hero-badge">OHIO'S SECTION 8 SPECIALISTS</div>
  <h1 class="abs hero-title">Managing the Properties Others <span>Won't Touch.</span></h1>
  <p class="abs hero-copy">Full-service Section 8 property management across Ohio — expert HAP contract management, first-attempt inspection passes, and deep LMHA relationships that work for you.</p>
  <div class="abs hero-actions">
    <span class="btn btn-red">Get a Free Consultation
      <svg width="12" height="12" viewBox="0 0 12 12" fill="none" stroke="#fff" stroke-width="1.6"><path d="M2 6h8M7 3l3 3-3 3"/></svg></span>
    <span class="btn btn-ghost">Explore Services</span>
  </div>
  <div class="abs stat-box">
    <div><div class="stat-num">500+</div><div class="stat-lbl">Properties Managed</div></div>
    <div><div class="stat-num">98%</div><div class="stat-lbl">First-Attempt Pass Rate</div></div>
    <div><div class="stat-num">15+</div><div class="stat-lbl">Years Experience</div></div>
    <div><div class="stat-num">LMHA</div><div class="stat-lbl">Certified Partner</div></div>
  </div>
</header>

<div class="abs trust">
  <span><i></i>LICENSED IN OHIO</span><span><i></i>LMHA CERTIFIED PARTNER</span><span><i></i>HARBOR OFFICE VERIFIED</span><span><i></i>HQS INSPECTION SPECIALISTS</span><span><i></i>HAP CONTRACT EXPERTS</span>
</div>

<section>
  <div class="abs about-photo-a" role="img" aria-label="Handshake over a small model house"></div>
  <div class="abs about-photo-b" role="img" aria-label="Two-storey suburban house with a car in the driveway"></div>
  <div class="abs about-badge"><b>98%</b><small>First-attempt inspection pass rate</small></div>
  <div class="abs about-text">
    <div class="eyebrow">About Us</div>
    <h2 class="h2">Built for the Challenges Most Managers Avoid</h2>
    <p class="body">Tallgrove Vale Management was founded on a single premise: that property owners in Ohio's most challenging zip codes deserve exceptional professional management — and that done right, these properties can be among the most stable investments in the market.</p>
    <p class="body" style="margin-top:16px">We have cultivated direct relationships with the <b>Lakeshore Metropolitan Housing Authority (LMHA)</b> and the <b>regional Harbor office</b>, enabling us to navigate the Section 8 voucher process with speed and precision that other management companies simply cannot match.</p>
    <ul class="checks">
      <li><svg width="14" height="14" viewBox="0 0 14 14" fill="none" stroke="#c62430" stroke-width="1.4"><circle cx="7" cy="7" r="6"/><path d="M4.3 7.2l1.8 1.8 3.6-3.8"/></svg>LMHA &amp; Harbor Office Partnerships</li>
      <li><svg width="14" height="14" viewBox="0 0 14 14" fill="none" stroke="#c62430" stroke-width="1.4"><circle cx="7" cy="7" r="6"/><path d="M4.3 7.2l1.8 1.8 3.6-3.8"/></svg>First-Attempt HQS Inspection Expertise</li>
      <li><svg width="14" height="14" viewBox="0 0 14 14" fill="none" stroke="#c62430" stroke-width="1.4"><circle cx="7" cy="7" r="6"/><path d="M4.3 7.2l1.8 1.8 3.6-3.8"/></svg>Full HAP Contract Lifecycle Management</li>
      <li><svg width="14" height="14" viewBox="0 0 14 14" fill="none" stroke="#c62430" stroke-width="1.4"><circle cx="7" cy="7" r="6"/><path d="M4.3 7.2l1.8 1.8 3.6-3.8"/></svg>Transparent Monthly Owner Reporting</li>
    </ul>
    <span class="btn btn-navy" style="height:38px;padding:0 24px">Talk to Our Team
      <svg width="12" height="12" viewBox="0 0 12 12" fill="none" stroke="#fff" stroke-width="1.6"><path d="M2 6h8M7 3l3 3-3 3"/></svg></span>
  </div>
</section>

<section class="abs services">
  <div class="abs svc-head">
    <div class="eyebrow">Our Services</div>
    <h2 class="h2" style="margin-top:16px">Everything Your<br>Property Needs</h2>
  </div>
  <p class="abs svc-intro body">Every service is designed around the unique demands of Section 8 and voucher-assisted housing in Ohio — so you can focus on growing your portfolio while we handle the complexity.</p>
  <div class="abs svc-grid">
    <div class="card"><div class="card-icon on"><svg width="16" height="16" viewBox="0 0 16 16" fill="none" stroke="#fff" stroke-width="1.4"><circle cx="6" cy="5.5" r="2.5"/><path d="M1.5 13c.5-2.5 2.3-4 4.5-4s4 1.5 4.5 4M10.5 3.2a2.4 2.4 0 010 4.6M12 9.3c1.3.6 2.2 1.9 2.5 3.7"/></svg></div><h3>Tenant Sourcing &amp; Placement</h3><p>We identify and screen qualified Section 8 voucher holders through our direct relationships with LMHA and regional Harbor offices, matching the right tenants to your property quickly.</p></div>
    <div class="card"><div class="card-icon"><svg width="16" height="16" viewBox="0 0 16 16" fill="none" stroke="#1d2d59" stroke-width="1.4"><path d="M4 1.5h5.5L12.5 4.5V14.5H4z"/><path d="M6 8h4.5M6 10.5h4.5"/></svg></div><h3>HAP Contract Management</h3><p>From initial execution to annual renewals, we handle every detail of your Housing Assistance Payment contracts — protecting your income stream and keeping you fully compliant.</p></div>
    <div class="card"><div class="card-icon"><svg width="16" height="16" viewBox="0 0 16 16" fill="none" stroke="#1d2d59" stroke-width="1.4"><rect x="3" y="2.5" width="10" height="12" rx="1.5"/><path d="M6 2.5h4v2H6zM5.8 9l1.6 1.6 3-3.2"/></svg></div><h3>Inspection Coordination</h3><p>Our team prepares your property to pass HQS inspections on the first attempt. We know exactly what inspectors look for and eliminate issues before the appointment.</p></div>
    <div class="card"><div class="card-icon"><svg width="16" height="16" viewBox="0 0 16 16" fill="none" stroke="#1d2d59" stroke-width="1.4"><path d="M2.5 7.5L8 2.5l5.5 5V14h-11z"/><path d="M6.5 14v-4h3v4"/></svg></div><h3>Full-Service Leasing</h3><p>End-to-end leasing support including marketing, showings, applications, background checks, lease execution, and move-in coordination.</p></div>
    <div class="card"><div class="card-icon"><svg width="16" height="16" viewBox="0 0 16 16" fill="none" stroke="#1d2d59" stroke-width="1.4"><path d="M1.5 12l4.5-4.5 3 3 5-5.5M10.5 5h3.5v3.5"/></svg></div><h3>Owner Financial Reporting</h3><p>Transparent monthly statements, direct deposit disbursements, and year-end documentation so you always know exactly how your investment performs.</p></div>
    <div class="card"><div class="card-icon"><svg width="16" height="16" viewBox="0 0 16 16" fill="none" stroke="#1d2d59" stroke-width="1.4"><path d="M8 1.5l5.5 2v4.5c0 3.3-2.4 5.6-5.5 6.5-3.1-.9-5.5-3.2-5.5-6.5V3.5z"/></svg></div><h3>Maintenance &amp; Compliance</h3><p>24/7 maintenance coordination, vendor management, and proactive inspections to protect your asset and keep residents in safe, code-compliant homes.</p></div>
  </div>
</section>

<section>
  <div class="abs process-head">
    <div class="eyebrow">How It Works</div>
    <h2 class="h2">Our Proven Process</h2>
    <p class="body">A clear, repeatable system that protects your investment from day<br>one through long-term tenancy.</p>
  </div>
  <div class="abs steps">
    <div class="step"><div class="step-num on">01</div><h4>Property Assessment</h4><p>We evaluate your property against HQS standards and local housing authority requirements, identifying any issues before they become failures.</p></div>
    <div class="step"><div class="step-num">02</div><h4>Tenant Matching</h4><p>Using our LMHA and Harbor office relationships, we source pre-screened voucher holders whose payment size fits your unit's fair market rent.</p></div>
    <div class="step"><div class="step-num">03</div><h4>Lease &amp; HAP Execution</h4><p>We prepare all documentation, execute the lease alongside the HAP contract, and ensure the housing authority approves payments before move-in.</p></div>
    <div class="step"><div class="step-num">04</div><h4>Inspection &amp; Approval</h4><p>We coordinate and attend the HQS inspection, addressing any items on-the-spot and following up to secure approval quickly.</p></div>
    <div class="step"><div class="step-num">05</div><h4>Ongoing Management</h4><p>From rent collection and maintenance to annual HAP renewals and re-inspections, we handle everything so you collect your check each month.</p></div>
  </div>
  <div class="abs cta-band">
    <div><h3>Ready to Maximize Your Property's Potential?</h3><p>First consultation is always free. No obligation.</p></div>
    <span class="btn btn-red">Contact Us Today
      <svg width="12" height="12" viewBox="0 0 12 12" fill="none" stroke="#fff" stroke-width="1.6"><path d="M2 6h8M7 3l3 3-3 3"/></svg></span>
  </div>
</section>

<section class="abs stories">
  <div class="abs stories-head">
    <div class="eyebrow">Client Stories</div>
    <h2 class="h2">What<br>Owners Are<br>Saying</h2>
  </div>
  <div class="abs arrows">
    <span class="arrow"><svg width="10" height="10" viewBox="0 0 10 10" fill="none" stroke="#1a2238" stroke-width="1.5"><path d="M6.5 2L3.5 5l3 3"/></svg></span>
    <span class="arrow"><svg width="10" height="10" viewBox="0 0 10 10" fill="none" stroke="#1a2238" stroke-width="1.5"><path d="M3.5 2l3 3-3 3"/></svg></span>
  </div>
  <div class="abs dots"><i class="on"></i><i></i><i></i><i></i></div>
  <div class="abs quote-card">
    <div class="stars">
      <svg width="14" height="14" viewBox="0 0 14 14"><path fill="#c62430" d="M7 1l1.8 3.8 4.2.5-3.1 2.9.8 4.1L7 10.3 3.3 12.3l.8-4.1L1 5.3l4.2-.5z"/></svg>
      <svg width="14" height="14" viewBox="0 0 14 14"><path fill="#c62430" d="M7 1l1.8 3.8 4.2.5-3.1 2.9.8 4.1L7 10.3 3.3 12.3l.8-4.1L1 5.3l4.2-.5z"/></svg>
      <svg width="14" height="14" viewBox="0 0 14 14"><path fill="#c62430" d="M7 1l1.8 3.8 4.2.5-3.1 2.9.8 4.1L7 10.3 3.3 12.3l.8-4.1L1 5.3l4.2-.5z"/></svg>
      <svg width="14" height="14" viewBox="0 0 14 14"><path fill="#c62430" d="M7 1l1.8 3.8 4.2.5-3.1 2.9.8 4.1L7 10.3 3.3 12.3l.8-4.1L1 5.3l4.2-.5z"/></svg>
      <svg width="14" height="14" viewBox="0 0 14 14"><path fill="#c62430" d="M7 1l1.8 3.8 4.2.5-3.1 2.9.8 4.1L7 10.3 3.3 12.3l.8-4.1L1 5.3l4.2-.5z"/></svg>
    </div>
    <p class="quote">"Tallgrove Vale Management turned a property I nearly gave up on into a consistent income stream. They placed a Section 8 tenant within three weeks, handled every HAP form, and passed the LMHA inspection on the first try."</p>
    <div class="author"><span class="avatar">D</span><div><b>Daniel R.</b><small>Cleveland, OH</small></div></div>
  </div>
</section>

<section>
  <div class="abs contact-head">
    <div class="eyebrow">Get in Touch</div>
    <h2 class="h2">Let's Talk About<br>Your Properties</h2>
    <p class="body">Whether you have one unit or a full portfolio, we're ready to put our Section 8 expertise to work for you. First consultation is always free.</p>
  </div>
  <div class="abs contact-list">
    <div class="c-item"><span class="c-icon"><svg width="14" height="14" viewBox="0 0 14 14" fill="none" stroke="#1d2d59" stroke-width="1.3"><path d="M3 1.5h2l1 3-1.5 1a7 7 0 003.5 3.5l1-1.5 3 1v2c0 .6-.4 1-1 1A10.5 10.5 0 012 2.5c0-.6.4-1 1-1z"/></svg></span><div><small>PHONE</small><b>(614)<br>555-0147</b></div></div>
    <div class="c-item"><span class="c-icon"><svg width="14" height="14" viewBox="0 0 14 14" fill="none" stroke="#1d2d59" stroke-width="1.3"><rect x="1.5" y="3" width="11" height="8" rx="1"/><path d="M1.5 3.5L7 7.5l5.5-4"/></svg></span><div><small>EMAIL</small><b>info@tallgrovevalemgmt.<br>com</b></div></div>
    <div class="c-item"><span class="c-icon"><svg width="14" height="14" viewBox="0 0 14 14" fill="none" stroke="#1d2d59" stroke-width="1.3"><path d="M7 13s4.5-4 4.5-7.5a4.5 4.5 0 00-9 0C2.5 9 7 13 7 13z"/><circle cx="7" cy="5.5" r="1.6"/></svg></span><div><small>OFFICE</small><b>Columbus, Ohio — Serving All of Ohio</b></div></div>
  </div>
  <div class="abs form">
    <h3>Free Consultation Request</h3>
    <div class="row">
      <div class="field"><label>FULL NAME <span style="color:#c62430">*</span></label><div class="input">Ryan Whitaker</div></div>
      <div class="field"><label>PHONE</label><div class="input">(614) 555-0100</div></div>
    </div>
    <div class="field"><label>EMAIL ADDRESS <span style="color:#c62430">*</span></label><div class="input">ryan@example.com</div></div>
    <div class="field"><label>ABOUT YOUR PROPERTIES</label><div class="input tall">How many units do you own? What zip codes? Are they currently Section 8 or are you looking to convert?</div></div>
    <div class="submit">Send My Request</div>
    <p class="form-note">We respond within one business day. No obligation, ever.</p>
  </div>
</section>

<footer class="abs footer">
  <div class="abs f-brand">
    <div class="brand"><span class="brand-dot"></span>Tallgrove Vale Management</div>
    <p>Ohio's trusted Section 8 property management specialists. Turning challenging properties into consistent returns since 2009.</p>
  </div>
  <div class="abs f-col" style="left:440px">
    <h5>NAVIGATION</h5>
    <ul><li>About</li><li>Services</li><li>Process</li><li>Testimonials</li><li>Contact</li></ul>
  </div>
  <div class="abs f-col" style="left:801px">
    <h5>CONTACT</h5>
    <ul><li><i></i>(614) 555-0147</li><li><i></i>info@tallgrovevalemgmt.com</li><li><i></i>Columbus, Ohio — Serving All of Ohio</li></ul>
  </div>
  <div class="abs f-bottom"><span>© 2026 Tallgrove Vale Management. All rights reserved.</span><span>LMHA Certified · Harbor Office Partner · Licensed in Ohio</span></div>
</footer>

</body>
</html>
```